Swimming Pool Supply Company Business Cards

We need business cards designed for company. These need to be easy to edit so that we can fill in names, titles, and contact info for each person who works here.

Dalton R. Whitfield
Manager of Legal & Finance
K.L. Brisbane, Incorporated

4837 Grenway Avenue
Marlow Heights, PA 19243

E. dalton@klbrisbane-example.com
M. (215) 555-0173
O. (215) 555-0148

Contact Information for Business Card

Looking to upgrade current business cards with graphic that can be edited. Looking for fresh ideas for an age old industry.

Font styles to use
Serif
Sans Serif

Colors

Designer to choose colors to be used in the design.

Requirements
Must have
• Professional, fresh, unique but professional

```html
<!DOCTYPE html>
<html lang="en">
<head>
<meta charset="utf-8">
<title>K.L. Brisbane Business Cards</title>
<link href="https://fonts.googleapis.com/css2?family=Open+Sans:wght@400;600&family=Roboto:wght@400;500;700&family=Roboto+Condensed:wght@400;700&display=swap" rel="stylesheet">
<style>
  :root {
    --backdrop: #e6e3df;
    --card: #f7f7f7;
    --ink: #1b1b1b;
    --muted: #6f6f6f;
    --band: #c9c9c9;
    --rule: #111111;
    --icon-dark: #222222;
    --icon-light: #cfcfcf;
  }
  * { box-sizing: border-box; margin: 0; padding: 0; }
  html, body { width: 1200px; height: 886px; overflow: hidden; }
  body {
    background: var(--backdrop);
    position: relative;
    font-family: "Roboto", Arial, sans-serif;
    color: var(--ink);
  }
  .card {
    position: absolute;
    width: 620px;
    height: 354px;
    background: var(--card);
    box-shadow: 0 6px 18px rgba(0,0,0,0.18);
  }
  .card--front { left: 80px; top: 70px; }
  .card--back { left: 500px; top: 462px; }

  /* Front */
  .brand {
    position: absolute;
    left: 0; right: 0; top: 104px;
    text-align: center;
  }
  .brand__name {
    font-family: "Roboto", Arial, sans-serif;
    font-weight: 700;
    font-size: 58px;
    letter-spacing: 2px;
    line-height: 1;
    color: var(--ink);
  }
  .brand__tagline {
    font-family: "Open Sans", Arial, sans-serif;
    font-size: 14px;
    margin-top: 8px;
    color: var(--ink);
  }
  .front__web {
    position: absolute;
    left: 0; right: 0; bottom: 46px;
    text-align: center;
    font-family: "Open Sans", Arial, sans-serif;
    font-size: 12px;
    letter-spacing: 6px;
    color: #444;
  }

  /* Back */
  .rule {
    position: absolute;
    left: 0; right: 0;
    height: 4px;
    background: var(--rule);
  }
  .rule--top { top: 34px; }
  .rule--bottom { top: 174px; }
  .identity {
    position: absolute;
    left: 190px; top: 34px;
    width: 236px; height: 144px;
    background: var(--band);
    display: flex;
    flex-direction: column;
    justify-content: center;
    align-items: center;
    text-align: center;
  }
  .identity__name {
    font-family: "Roboto Condensed", Arial, sans-serif;
    font-weight: 700;
    font-size: 21px;
    letter-spacing: 0.5px;
    margin-bottom: 4px;
  }
  .identity__title,
  .identity__company {
    font-family: "Roboto Condensed", Arial, sans-serif;
    font-weight: 700;
    font-size: 14px;
    line-height: 1.3;
  }
  .contact {
    position: absolute;
    top: 216px;
    display: flex;
    flex-direction: column;
    align-items: center;
    text-align: center;
    font-size: 14px;
    line-height: 1.35;
    color: var(--muted);
  }
  .contact--address { left: 40px; width: 210px; }
  .contact--phone { left: 270px; width: 150px; }
  .contact--email { left: 400px; width: 210px; }
  .contact__icon { width: 34px; height: 34px; margin-bottom: 12px; }
</style>
</head>
<body>

  <section class="card card--front">
    <div class="brand">
      <div class="brand__name">BRISBANE</div>
      <div class="brand__tagline">Big Enough to Serve You, Small Enough to Care</div>
    </div>
    <div class="front__web">www.klbrisbane-example.com</div>
  </section>

  <section class="card card--back">
    <div class="rule rule--top"></div>
    <div class="rule rule--bottom"></div>

    <div class="identity">
      <div class="identity__name">DALTON R. WHITFIELD</div>
      <div class="identity__title">Manager of Legal &amp; Finance</div>
      <div class="identity__company">K.L. Brisbane, Incorporated</div>
    </div>

    <div class="contact contact--address">
      <svg class="contact__icon" viewBox="0 0 34 34" aria-hidden="true">
        <circle cx="17" cy="17" r="17" fill="var(--icon-dark)"/>
        <path d="M17 8c-3.6 0-6.3 2.7-6.3 6.1 0 4.4 6.3 11.4 6.3 11.4s6.3-7 6.3-11.4C23.3 10.7 20.6 8 17 8z" fill="none" stroke="#fff" stroke-width="1.6"/>
        <circle cx="17" cy="14.2" r="2.2" fill="#fff"/>
      </svg>
      <span>4837 Grenway Avenue</span>
      <span>Marlow Heights, PA 19243</span>
    </div>

    <div class="contact contact--phone">
      <svg class="contact__icon" viewBox="0 0 34 34" aria-hidden="true">
        <circle cx="17" cy="17" r="17" fill="var(--icon-light)"/>
        <rect x="12.5" y="8.5" width="9" height="17" rx="1.5" fill="none" stroke="#555" stroke-width="1.6"/>
        <circle cx="17" cy="22.5" r="0.9" fill="#555"/>
      </svg>
      <span>(215) 555-0148</span>
      <span>(215) 555-0173</span>
    </div>

    <div class="contact contact--email">
      <svg class="contact__icon" viewBox="0 0 34 34" aria-hidden="true">
        <circle cx="17" cy="17" r="17" fill="var(--icon-dark)"/>
        <rect x="10" y="12" width="14" height="10" fill="#fff"/>
        <path d="M10 12l7 6 7-6" fill="none" stroke="var(--icon-dark)" stroke-width="1.4"/>
      </svg>
      <span>dalton@klbrisbane-example.com</span>
      <span>www.klbrisbane-example.com</span>
    </div>
  </section>

</body>
</html>
```